Business Postcard Mailer - 2 sided - 6 x 10.5 inches

We will be purchasing multiple designs through this project. We need a postcard mailer for a residential painting business. The final design needs to have the special 15% Off, contact information, company logo, stamp indicia, and list of services. I will provide past examples and any additional logos. Company colors are #34482E and #4A1717. Old samples are provided. Final flat size should be 6 x 10.5 inches. And we will need a return address in the upper left-hand corner of the backside. QMRB Layout Guidelines are attached. 4389 Juniper Ave #7, Waukesha, WI 53947.
Updates

I just guaranteed the project and will be expecting more entries. We will also be purchasing additional designs (4-5) so we want to ensure a good variety.

Target Market(s)

Homeowners

Industry/Entity Type

Painting

Font styles to use
Sans Serif

Requirements
Must have
• Logo and brand colors
Nice to have
• Call to action - Book your free estimate at www.BrightCoatCrew.example or Call now 262-555-0147.

```html
<!DOCTYPE html>
<html lang="en">
<head>
<meta charset="utf-8">
<title>Bright Coat Painting – Postcard Mailer</title>
<link rel="stylesheet" href="https://fonts.googleapis.com/css2?family=Montserrat:wght@400;500;600;700&family=Roboto+Slab:wght@400;700&family=Roboto+Condensed:wght@500&display=swap">
<style>
  :root {
    --green: #34482E;
    --maroon: #4A1717;
    --backdrop: #e4e4e4;
    --paper: #ffffff;
    --grey-panel: #d7d7d9;
    --ink: #222222;
    --muted: #9aa097;
  }
  * { box-sizing: border-box; margin: 0; padding: 0; }
  html, body { width: 1200px; height: 903px; overflow: hidden; background: var(--backdrop); }
  body { font-family: "Montserrat", sans-serif; color: var(--ink); }
  .stage { position: absolute; left: 0; top: 0; width: 1500px; height: 1129px; transform: scale(0.8); transform-origin: 0 0; }
  .card { position: absolute; background: var(--paper); box-shadow: 0 2px 6px rgba(0,0,0,.18); overflow: hidden; }
  .abs { position: absolute; white-space: nowrap; }

  /* brand lockup */
  .brand { position: absolute; display: flex; align-items: center; gap: 10px; white-space: nowrap; }
  .brand-mark { width: 20px; height: 20px; background: var(--maroon); flex: none; }
  .brand-name { font-weight: 700; color: var(--green); line-height: 1; letter-spacing: -0.5px; }
  .brand-name span { display: block; }

  /* front */
  .front { left: 170px; top: 60px; width: 860px; height: 490px; }
  .front .brand { left: 30px; top: 34px; }
  .front .brand-name { font-size: 30px; }
  .front-photo { left: 262px; top: 16px; width: 583px; height: 421px;
    clip-path: polygon(0 0, 100% 0, 100% 100%, 40px 100%);
    background: linear-gradient(180deg, #cfe1ee 0%, #7f8fa8 35%, #4b5878 55%, #6a7d45 75%, #5f8a35 100%); }
  .painter-photo { left: 222px; top: 116px; width: 150px; height: 321px;
    background: linear-gradient(180deg, #c9a184 0%, #2c3550 30%, #e9ecef 55%, #dfe3e6 100%); border-radius: 40px 40px 0 0; }
  .services { left: 16px; top: 127px; width: 272px; height: 124px; background: var(--green); padding: 6px 0 0 10px; }
  .services li, .service-list li { list-style: none; color: #fff; font-size: 14px; font-weight: 500; line-height: 22.8px; display: flex; align-items: center; gap: 8px; white-space: nowrap; }
  .services li::before, .service-list li::before { content: ""; width: 8px; height: 8px; border-radius: 50%; background: var(--muted); flex: none; }
  .local-band { left: 16px; top: 254px; width: 216px; height: 27px; background: var(--maroon); color: #fff;
    font-family: "Roboto Condensed", sans-serif; font-weight: 500; font-size: 14px; line-height: 27px; padding-left: 9px; }
  .offer { left: 16px; width: 196px; height: 70px; font-family: "Roboto Slab", serif; }
  .offer svg { position: absolute; left: 0; top: 0; }
  .offer .label { position: absolute; left: 9px; top: 6px; font-size: 15px; }
  .offer .amount { position: absolute; left: 9px; top: 26px; font-size: 19px; font-weight: 700; color: var(--maroon); }
  .offer .terms { position: absolute; left: 9px; top: 52px; font-size: 9px; }
  .or-badge { left: 203px; top: 342px; width: 36px; height: 36px; border-radius: 50%; background: var(--green); color: #fff;
    font-family: "Roboto Slab", serif; font-weight: 700; font-size: 17px; text-align: center; line-height: 32px; border: 2px solid #fff; }
  .cta-call { left: 16px; top: 437px; width: 290px; height: 38px; background: var(--green); color: #fff;
    clip-path: polygon(0 0, 280px 0, 290px 100%, 0 100%); display: flex; align-items: center; padding-left: 12px; gap: 12px; font-size: 15px; font-weight: 500; }
  .cta-book { left: 298px; top: 437px; width: 547px; height: 38px; background: var(--maroon); color: #fff;
    clip-path: polygon(0 0, 100% 0, 100% 100%, 10px 100%); display: flex; align-items: center; padding-left: 40px; gap: 12px; font-size: 15px; font-weight: 500; }
  .icon { flex: none; }

  /* back */
  .back { left: 531px; top: 578px; width: 861px; height: 492px; }
  .back .brand { left: 22px; top: 26px; }
  .back .brand-name { font-size: 28px; }
  .return-address { left: 33px; top: 97px; font-size: 13px; line-height: 15px; color: #444; font-style: normal; }
  .coupon { top: 24px; width: 244px; height: 100px; border: 2px dashed var(--maroon); text-align: center; font-family: "Roboto Slab", serif; }
  .coupon .amount { margin-top: 8px; font-size: 26px; font-weight: 700; color: var(--maroon); }
  .coupon .label { font-size: 20px; color: var(--green); margin-top: 2px; }
  .coupon .terms { font-size: 11.5px; font-weight: 700; margin-top: 8px; }
  .indicia { left: 734px; top: 25px; width: 97px; height: 97px; border: 2px solid #111; text-align: center; font-family: Arial, sans-serif; font-size: 12px; line-height: 13px; padding-top: 6px; }
  .indicia .paid { font-size: 16px; font-weight: 700; border-top: 1px solid #111; border-bottom: 1px solid #111; margin: 3px 8px; line-height: 20px; }
  .estimates { left: 0; top: 143px; width: 400px; height: 123px; background: var(--green); padding: 12px 0 0 33px; }
  .estimates h2 { font-family: "Roboto Slab", serif; font-weight: 700; font-size: 20px; color: #fff; margin-bottom: 6px; }
  .service-cols { display: flex; gap: 36px; }
  .service-list li { font-size: 14px; line-height: 20.5px; }
  .info-panel { left: 400px; top: 143px; width: 461px; height: 272px; background: var(--grey-panel); }
  .info-panel p { position: absolute; left: 32px; top: 28px; width: 420px; font-size: 13.5px; line-height: 17px; white-space: normal; }
  .mail-area { position: absolute; left: 32px; top: 99px; width: 408px; height: 160px; background: #fff; }
  .photo { top: 273px; height: 134px; }
  .photo-before { left: 16px; width: 190px; background: linear-gradient(180deg, #a9bcd0 0%, #e9ebe8 45%, #c6c9c2 70%, #6d7c5d 100%); }
  .photo-after { left: 211px; width: 190px; background: linear-gradient(180deg, #b8c8d8 0%, #4a5560 45%, #3b4450 70%, #6f7d62 100%); }
  .photo-tag { position: absolute; left: 0; top: 0; width: 70px; height: 50px; background: var(--maroon); clip-path: polygon(0 0, 100% 0, 0 100%); }
  .photo-tag span { position: absolute; left: 3px; top: 14px; transform: rotate(-35deg); color: #fff; font-size: 12px; }
  .contact-bar { left: 0; top: 415px; width: 400px; height: 77px; background: var(--maroon); color: #fff; }
  .contact-bar .row1 { position: absolute; left: 19px; top: 16px; display: flex; align-items: center; gap: 7px; font-size: 14px; font-weight: 500; white-space: nowrap; }
  .contact-bar .email { font-size: 11.5px; font-weight: 400; margin-left: 8px; display: flex; align-items: center; gap: 5px; }
  .contact-bar .row2 { position: absolute; left: 21px; top: 46px; display: flex; align-items: center; gap: 8px; font-size: 11.5px; font-weight: 500; white-space: nowrap; }
  .badges { left: 460px; top: 432px; display: flex; gap: 14px; align-items: center; }
  .badge { background: #b9bcb8; }
  .footer-line { left: 425px; top: 485px; width: 436px; height: 7px; background: var(--green); }
</style>
</head>
<body>
<div class="stage">

  <section class="card front">
    <div class="abs front-photo" role="img" aria-label="Photo of a blue craftsman-style house with a stone walkway and green lawn"></div>
    <div class="abs painter-photo" role="img" aria-label="Photo of a smiling painter in white overalls holding a paint bucket"></div>

    <div class="brand"><span class="brand-mark"></span><span class="brand-name"><span>Bright Coat</span><span>Painting</span></span></div>

    <ul class="abs services">
      <li>Interior Painting</li>
      <li>Exterior Painting</li>
      <li>Carpentry Services</li>
      <li>Drywall Repair</li>
      <li>Color Consultations</li>
    </ul>
    <div class="abs local-band">Locally Owned and Operated</div>

    <div class="abs offer" style="top:285px">
      <svg width="196" height="70"><path d="M1 1H170L195 35L170 69H1Z" fill="none" stroke="#666" stroke-dasharray="2 2"/></svg>
      <span class="label">Winter Special</span>
      <span class="amount">25% OFF</span>
      <span class="terms">December - February, Interior Only</span>
    </div>
    <div class="abs offer" style="top:362px">
      <svg width="196" height="70"><path d="M1 1H170L195 35L170 69H1Z" fill="none" stroke="#666" stroke-dasharray="2 2"/></svg>
      <span class="label">Spring Special</span>
      <span class="amount">15% OFF</span>
      <span class="terms">Starting March, Interior &amp; Exterior</span>
    </div>
    <div class="abs or-badge">OR</div>

    <div class="abs cta-call">
      <span>CALL NOW</span>
      <svg class="icon" width="16" height="16" viewBox="0 0 16 16"><path d="M3 1l3 3-2 2c1 2 3 4 5 5l2-2 3 3-2 3C7 14 2 9 1 3z" fill="none" stroke="#fff" stroke-width="1.3"/></svg>
      <span>262-555-0147</span>
    </div>
    <div class="abs cta-book">
      <span>or Book your free estimate at</span>
      <svg class="icon" width="12" height="12" viewBox="0 0 12 12"><circle cx="6" cy="6" r="5" fill="none" stroke="#fff"/><path d="M1 6h10M6 1c-3 3-3 7 0 10M6 1c3 3 3 7 0 10" fill="none" stroke="#fff" stroke-width=".8"/></svg>
      <span>www.BrightCoatCrew.example</span>
    </div>
  </section>

  <section class="card back">
    <div class="brand"><span class="brand-mark"></span><span class="brand-name"><span>Bright Coat</span><span>Painting</span></span></div>
    <address class="abs return-address">4389 Juniper Ave #7,<br>Waukesha, WI 53947</address>

    <div class="abs coupon" style="left:216px">
      <div class="amount">25% OFF</div>
      <div class="label">Winter Special</div>
      <div class="terms">December - February, Interior Only</div>
    </div>
    <div class="abs coupon" style="left:472px">
      <div class="amount">15% OFF</div>
      <div class="label">Spring Special</div>
      <div class="terms">Starting March, Interior &amp; Exterior</div>
    </div>
    <div class="abs indicia">Presorted<br>Standard<br>U.S. Postage<div class="paid">PAID</div>QMRB</div>

    <div class="abs estimates">
      <h2>Free Estimates</h2>
      <div class="service-cols">
        <ul class="service-list"><li>Interior Painting</li><li>Exterior Painting</li><li>Carpentry Services</li></ul>
        <ul class="service-list"><li>Drywall Repair</li><li>Color Consultations</li></ul>
      </div>
    </div>

    <div class="abs info-panel">
      <p>We cater the size of the crew to the size of the job and work full continuous days until the project is complete.</p>
      <div class="mail-area"></div>
    </div>

    <div class="abs photo photo-before" role="img" aria-label="Before photo of a white two-storey house during painting"><div class="photo-tag"><span>Before</span></div></div>
    <div class="abs photo photo-after" role="img" aria-label="After photo of the same house painted dark grey"><div class="photo-tag"><span>After</span></div></div>

    <div class="abs contact-bar">
      <div class="row1">
        <span>CALL NOW</span>
        <svg class="icon" width="14" height="14" viewBox="0 0 16 16"><path d="M3 1l3 3-2 2c1 2 3 4 5 5l2-2 3 3-2 3C7 14 2 9 1 3z" fill="none" stroke="#fff" stroke-width="1.3"/></svg>
        <span>262-555-0147</span>
        <span class="email"><svg class="icon" width="10" height="8" viewBox="0 0 10 8"><rect x=".5" y=".5" width="9" height="7" fill="none" stroke="#fff"/><path d="M.5.5L5 4 9.5.5" fill="none" stroke="#fff"/></svg>hello@brightcoat.example</span>
      </div>
      <div class="row2">
        <span>or Book your free estimate at</span>
        <svg class="icon" width="10" height="10" viewBox="0 0 12 12"><circle cx="6" cy="6" r="5" fill="none" stroke="#fff"/></svg>
        <span>www.BrightCoatCrew.example</span>
      </div>
    </div>

    <div class="abs badges" aria-label="Membership badges">
      <div class="badge" style="width:22px;height:34px"></div>
      <div class="badge" style="width:32px;height:32px"></div>
      <div class="badge" style="width:42px;height:30px"></div>
      <div class="badge" style="width:64px;height:28px"></div>
      <div class="badge" style="width:44px;height:30px"></div>
      <div class="badge" style="width:80px;height:30px"></div>
    </div>
    <div class="abs footer-line"></div>
  </section>

</div>
</body>
</html>
```